Tidal-Cup Coffee Kiosks Webdesign project

Tidal-Cup Coffee Kiosks provides coffee carts, kiosks, and/or drive thrus depending on location. At Tidal-Cup our company focuses on offering healthy snack & drink options for people on the go as well as nutritional coaching with our daily "Cup notes." We will provide some healthy snacks as well.

We offer all organic coffee & espresso drinks,100% real fruit & vegetable smoothies, protein shakes, and healthy breakfast/snack items.

I want "balance" to be a big theme in the website design. True well-being is a balance of body (health), mind (emotional well-being) and spirit (we are a Christian based company who loves and accepts all people, sexual orientation, religions, ect)

My parents are missionaries and founded the Nicaraguan organization "Bright Harvest Outreach Nicaragua" over 11 years ago ( www.brightharvestout.org ). Tidal-Cup plans to be a financial partner to their mission so 10% of profits or 2% of total revenue, whichever is greater will go to Bright Harvest and their church plants & medical/dental clinic. I want this and info about Bright Harvest to have a page on the website.
Updates

Target Market(s)

Ages 18-54 (target coffee customer).

Industry/Entity Type

Financial

Requirements
Must have
• -Home page
-Menu page
-Locations page/contact page
-Kiosk options page (cart, kiosk & drive thru descriptions, pics, traffic & location needs, ect)
-Fundraising/Bright Harvest Outreach Nicaragua page
Nice to have
• I have a logo designed that I attached. I would like the colors to be dark brown, light brown, and a lime green. My business card is also attached.

```html
<!DOCTYPE html>
<html lang="en">
<head>
<meta charset="utf-8">
<title>Tidal-Cup Coffee Kiosks</title>
<link href="https://fonts.googleapis.com/css2?family=Yanone+Kaffeesatz:wght@300;400;600;700&display=swap" rel="stylesheet">
<style>
:root{
  --lime:#a4cb3f;
  --lime-dark:#8fb52e;
  --espresso:#3b1d0e;
  --roast:#7d3a20;
  --roast-mid:#974b27;
  --roast-deep:#6a321c;
  --cream:#fff7ea;
  --latte:#e3b98a;
  --tan:#c89366;
  --white:#ffffff;
}
*{margin:0;padding:0;box-sizing:border-box}
html,body{width:1200px;height:747px;overflow:hidden}
body{font-family:"Yanone Kaffeesatz",sans-serif;background:var(--roast);color:var(--white);position:relative}

.top-bar{position:absolute;left:0;top:0;width:1200px;height:50px;background:var(--lime)}
.main-nav{position:absolute;top:0;left:0;width:1200px;height:50px}
.main-nav a{position:absolute;top:14px;color:var(--cream);text-decoration:none;font-size:20px;font-weight:300;letter-spacing:.5px;text-shadow:0 1px 1px rgba(0,0,0,.25)}
.main-nav .current-marker{position:absolute;left:500px;top:0;width:0;height:0;border-left:9px solid transparent;border-right:9px solid transparent;border-top:8px solid var(--espresso)}

.brand{position:absolute;left:232px;top:4px;width:120px;text-align:center;z-index:3}
.brand-dot{display:block;width:40px;height:40px;border-radius:50%;background:var(--espresso);margin:0 auto 2px}
.brand-name{font-size:30px;font-weight:600;color:var(--white);line-height:1}

.hero{position:absolute;left:0;top:50px;width:1200px;height:387px;
  background:radial-gradient(ellipse at 50% 60%,#6b3a1c 0%,#4a2510 55%,#2e160a 100%)}
.hero-headline{position:absolute;left:298px;top:72px;width:618px;height:60px;background:rgba(45,22,9,.82);text-align:center;font-size:37px;font-weight:600;line-height:60px}
.hero-sub{position:absolute;left:298px;top:139px;width:618px;height:83px;background:rgba(45,22,9,.7);text-align:center;font-size:28px;font-weight:300;line-height:46px;padding-top:-4px}

.cup-photo{position:absolute;left:478px;top:340px;width:262px;height:160px;border-radius:50% 50% 46% 46%;
  background:radial-gradient(ellipse at 45% 40%,#f4f1ec 0%,#d9d4cc 55%,#b85a3a 85%,rgba(160,60,40,0) 100%);z-index:2}

.accent-line{position:absolute;left:0;top:437px;width:1200px;height:5px;background:var(--lime)}

.feature-band{position:absolute;left:0;top:442px;width:1200px;height:250px;
  background:radial-gradient(ellipse at 50% 30%,var(--roast-mid) 0%,var(--roast) 70%,#73361e 100%)}

.cup-notes{position:absolute;left:222px;top:472px;width:220px}
.cup-notes h2{font-size:24px;font-weight:400;line-height:28px;color:var(--white)}
.cup-notes p{margin-top:4px;font-size:23px;font-weight:300;line-height:24px;color:var(--latte)}
.read-more{position:absolute;left:352px;top:619px;width:85px;height:26px;border-radius:13px;
  background:linear-gradient(#e2b58c,#b4784c);color:var(--cream);font-size:15px;line-height:26px;text-align:center;text-decoration:none;box-shadow:0 2px 3px rgba(0,0,0,.35)}

.offer-list{position:absolute;left:470px;top:460px;width:270px;height:192px;border-left:1px solid rgba(230,160,110,.35);border-right:1px solid rgba(230,160,110,.35);list-style:none;padding-top:42px}
.offer-list li{height:29px;line-height:29px;text-align:center;font-size:20px;color:var(--cream);border-bottom:1px solid rgba(240,170,120,.25);background:rgba(70,30,12,.25)}
.offer-list li:first-child{background:rgba(50,20,8,.55)}

.mission-screen{position:absolute;left:758px;top:482px;width:228px;height:140px;border-radius:8px 8px 4px 4px;
  background:linear-gradient(#f2f2f2 0%,#d6d6d6 75%,#8e8e8e 100%)}
.mission-link{position:absolute;left:758px;top:630px;width:240px;text-align:center;font-size:13.5px;color:var(--cream);text-decoration:none}

.site-footer{position:absolute;left:0;top:692px;width:1200px;height:55px;background:var(--roast-deep)}
.copyright{position:absolute;left:229px;top:24px;font-size:12.5px;color:var(--cream)}
.connect{position:absolute;left:842px;top:24px;font-size:12.5px;color:var(--cream)}
.social{position:absolute;top:20px;width:22px;height:22px;border-radius:50%;background:var(--white)}
</style>
</head>
<body>
<header class="top-bar">
  <nav class="main-nav">
    <span class="current-marker"></span>
    <a href="#" style="left:491px">HOME</a>
    <a href="#" style="left:578px">MENU</a>
    <a href="#" style="left:664px">CONTACT</a>
    <a href="#" style="left:762px">KIOSK OPTIONS</a>
    <a href="#" style="left:894px">FUNDRAISING</a>
  </nav>
</header>
<div class="brand"><span class="brand-dot"></span><span class="brand-name">Tidal-Cup</span></div>

<section class="hero" role="img" aria-label="Background of roasted coffee beans">
  <h1 class="hero-headline">We offer all organic coffee &amp; espresso drinks</h1>
  <p class="hero-sub">100% real fruit &amp; vegetable smoothies, protein shakes, and<br>healthy breakfast/snack items.</p>
</section>
<div class="accent-line"></div>

<section class="feature-band">
</section>
<div class="cup-photo" role="img" aria-label="Cappuccino cup on a saucer with red coffee cherries"></div>

<article class="cup-notes">
  <h2>DAILY “CUP NOTES”</h2>
  <p>Despite what most people think, an espresso has 1/3 the caffeine of a cup of coffee due to serving sizes</p>
</article>
<a class="read-more" href="#">READ MORE</a>

<ul class="offer-list">
  <li>ORGANIC COFFEE</li>
  <li>EXPRESSO DRINKS</li>
  <li>SMOOTHIES</li>
  <li>PROTEIN SHAKERS</li>
  <li>HEALTHY SNACK</li>
</ul>

<div class="mission-screen" role="img" aria-label="Laptop showing the Bright Harvest Outreach Nicaragua website"></div>
<a class="mission-link" href="#">FIND OUT MORE ABOUT BRIGHT HARVEST</a>

<footer class="site-footer">
  <p class="copyright">© 2006-2013 TIDAL-CUP COFFEE, ALL RIGHTS RESERVED</p>
  <p class="connect">CONNECT WITH US</p>
  <a class="social" href="#" style="left:933px" aria-label="Social network one"></a>
  <a class="social" href="#" style="left:963px" aria-label="Social network two"></a>
</footer>
</body>
</html>
```